New Website for Consulting Company

Our company needs a fresh web design to help us drive our business forward. We are a consulting and software provider to Airports, Air Traffic Organizations, Builders and Architects. We specialize in analyzing operations, monitoring noise levels and creating software to improve operations, meet customer requirements and improve public relations.
Additional Info:
- Additional requirements can be found in the Web Design Brief
- Logo and logo branding attached
Target Market(s)
Airlines, Airports, Government Agencies, and Real Estate Developers
Industry/Entity Type
Aviation
Coding
Coded - Design and coding required
Number of Pages Required
2 page
Colors
Designer to choose colors to be used in the design.
Requirements
Must have
- - Create a Wordpress Design (Coded - Design and coding required)
- - Designer must provide full implementation/coding depending on the platform chosen by the client (i.e. Wordpress theme, HTML/CSS, etc.)
- - This is a multi-page site; Supporting pages can be formatted the same, but links need to be in place
- - Colors used must be grey scale, black or match the logo. It is not necessary to use all the colors in our logo
Should not have
- We are not looking for an overly bright site. While our logo has 5 different colors, it is not necessary to use all of them.

```html
<!DOCTYPE html>
<html lang="en">
<head>
<meta charset="utf-8">
<title>SkyGrid International</title>
<link rel="stylesheet" href="https://fonts.googleapis.com/css2?family=Montserrat:wght@400;600;700;800&family=Open+Sans:wght@400;600;700&display=swap">
<style>
:root{
  --navy:#0b2545;
  --navy-deep:#071a33;
  --blue:#1d63ad;
  --sky:#3d8fd9;
  --ink:#222a33;
  --text:#55606b;
  --muted:#8a949e;
  --paper:#ffffff;
  --grey-bg:#eef1f4;
  --footer:#0d1f36;
  --footer-bar:#08152a;
}
*{box-sizing:border-box;margin:0;padding:0}
html,body{width:1200px;height:2512px;overflow:hidden}
body{font-family:"Open Sans",Arial,sans-serif;color:var(--text);background:var(--paper);position:relative}
h1,h2,h3,h4{font-family:"Montserrat",Arial,sans-serif}

.hero{position:absolute;left:0;top:0;width:1200px;height:420px;overflow:hidden}
.hero-bg{position:absolute;inset:0;background:
  radial-gradient(ellipse 520px 160px at 600px 360px,rgba(255,190,110,.85),rgba(255,150,80,.2) 60%,transparent 80%),
  linear-gradient(180deg,#0a2a5a 0%,#1a4f8f 40%,#3e7ab8 62%,#c48a5e 86%,#3a2c2a 100%)}
.site-header{position:absolute;left:0;top:0;width:1200px;height:72px;display:flex;align-items:center;justify-content:space-between;padding:0 160px 0 170px}
.brand{display:flex;align-items:center;gap:10px;font-family:"Montserrat",sans-serif;font-weight:800;font-size:26px;color:#fff}
.brand-dot{width:14px;height:14px;border-radius:50%;background:#fff}
.main-nav{display:flex;gap:4px;align-items:center}
.main-nav a{font-family:"Montserrat",sans-serif;font-size:11px;font-weight:600;color:#fff;text-decoration:none;padding:8px 12px;letter-spacing:.5px}
.main-nav a.active{background:rgba(255,255,255,.15)}
.hero-title{position:absolute;top:108px;width:100%;text-align:center;color:#fff;font-size:44px;font-weight:800;letter-spacing:1px}
.hero-sub{position:absolute;top:166px;left:340px;width:520px;text-align:center;color:#fff;font-size:14px;line-height:20px}
.btn{display:inline-block;background:var(--blue);color:#fff;font-family:"Montserrat",sans-serif;font-weight:600;font-size:13px;padding:12px 28px;text-decoration:none;letter-spacing:.5px}
.hero .btn{position:absolute;top:290px;left:538px}
.hero-arrow{position:absolute;top:278px;width:30px;height:56px;background:rgba(0,0,0,.4)}
.hero-arrow.left{left:0}.hero-arrow.right{right:0}
.hero-arrow svg{position:absolute;left:9px;top:20px}

.about{position:absolute;top:420px;left:0;width:1200px;height:660px}
.eyebrow{font-family:"Open Sans",sans-serif;font-style:italic;font-size:13px;color:var(--blue)}
.section-title{font-size:30px;font-weight:800;color:var(--navy);letter-spacing:.5px}
.about-copy{position:absolute;left:120px;top:70px;width:470px}
.about-copy .rule{width:50px;height:3px;background:var(--blue);margin:8px 0 18px}
.about-copy p{font-size:12.5px;line-height:19px;margin-bottom:12px}
.about-copy p b{color:var(--ink)}
.about-copy .btn{margin-top:120px}
.about-visual{position:absolute;left:630px;top:90px;width:500px;height:380px;border-radius:50%;
  background:radial-gradient(ellipse at 50% 50%,#d7ecfb 0%,#a9d3f2 55%,rgba(169,211,242,0) 72%)}
.about-brand{position:absolute;left:880px;top:500px;font-family:"Montserrat",sans-serif;font-weight:800;font-size:30px;color:var(--navy)}

.services{position:absolute;top:1080px;left:0;width:1200px;height:360px;
  background:linear-gradient(180deg,var(--navy) 0%,#13437c 100%)}
.services .eyebrow{color:#9fc6ee;text-align:center;display:block;margin-top:46px}
.services .section-title{color:#fff;text-align:center;margin-top:4px}
.services .rule{width:50px;height:3px;background:var(--sky);margin:10px auto 0}
.service-grid{position:absolute;left:120px;top:150px;width:960px;display:flex;gap:16px}
.service-card{width:228px}
.service-img{height:150px;border:3px solid #fff}
.service-card:nth-child(1) .service-img{background:linear-gradient(160deg,#6aa9e0,#2b5e93 60%,#7b6a58)}
.service-card:nth-child(2) .service-img{background:linear-gradient(160deg,#1b3857,#2f6aa5 55%,#c9d7e6)}
.service-card:nth-child(3) .service-img{background:linear-gradient(160deg,#0f2238,#4c6f95 55%,#d9d2c4)}
.service-card:nth-child(4) .service-img{background:linear-gradient(160deg,#1a3a5c,#3e86c4 55%,#e6e3df)}
.service-label{display:flex;align-items:center;justify-content:center;background:var(--navy-deep);color:#fff;font-family:"Montserrat",sans-serif;font-weight:700;font-size:12px;height:34px;letter-spacing:.5px}

.goals{position:absolute;top:1440px;left:0;width:1200px;height:280px;display:flex;padding:50px 120px 0;gap:60px}
.goal-col{flex:1}
.goal-col h3{font-size:22px;font-weight:700;color:var(--navy)}
.goal-col .rule{width:40px;height:3px;background:var(--blue);margin:10px 0 22px}
.goal-col ul{list-style:none}
.goal-col li{position:relative;padding-left:18px;font-size:12.5px;line-height:19px;margin-bottom:12px}
.goal-col li::before{content:"";position:absolute;left:0;top:6px;width:7px;height:7px;background:var(--blue)}

.news{position:absolute;top:1720px;left:0;width:1200px;height:440px;background:var(--grey-bg)}
.news-bg{position:absolute;inset:0;background:linear-gradient(90deg,rgba(205,214,224,.7),rgba(238,241,244,.2) 35%,rgba(238,241,244,.2) 65%,rgba(205,214,224,.7))}
.news .eyebrow{display:block;text-align:center;margin-top:30px;position:relative}
.news .section-title{text-align:center;position:relative;margin-top:2px}
.news .rule{width:50px;height:3px;background:var(--blue);margin:8px auto 0;position:relative}
.news-grid{position:absolute;left:220px;top:128px;width:760px;display:flex;gap:20px}
.news-card{width:240px}
.news-img{height:150px}
.news-card:nth-child(1) .news-img{background:linear-gradient(160deg,#b7c3ce,#6d7f90)}
.news-card:nth-child(2) .news-img{background:linear-gradient(160deg,#5d86b5,#21466f)}
.news-card:nth-child(3) .news-img{background:linear-gradient(180deg,#f2b35c,#c0652e 55%,#3a2a22)}
.news-card h4{font-size:15px;font-weight:700;color:var(--ink);line-height:20px;margin-top:16px}
.news-meta{display:flex;gap:10px;margin-top:10px;font-size:9.5px;color:var(--muted)}
.news-meta span::before{content:"";display:inline-block;width:6px;height:6px;border-radius:50%;background:var(--blue);margin-right:4px;vertical-align:1px}

.site-footer{position:absolute;top:2160px;left:0;width:1200px;height:320px;background:var(--footer);display:flex;padding:48px 120px 0;gap:40px}
.foot-col h4{font-size:12px;color:#fff;font-weight:700;letter-spacing:.5px}
.foot-col .rule{width:28px;height:2px;background:var(--sky);margin:6px 0 14px}
.foot-col p,.foot-col li{font-size:11px;line-height:18px;color:#a9b6c4;list-style:none}
.foot-about{width:290px}.foot-links{width:150px}.foot-services{width:170px}.foot-contact{width:200px}
.foot-col li::before{content:"\203A";color:var(--sky);margin-right:6px}
.contact-row{display:flex;gap:8px;align-items:flex-start}
.contact-row svg{flex:none;margin-top:4px}
.socials{display:flex;gap:8px;margin-top:14px}
.socials span{width:22px;height:22px;border-radius:50%;background:var(--blue)}
.foot-bar{position:absolute;top:2480px;left:0;width:1200px;height:32px;background:var(--footer-bar);color:#7d8a98;font-size:10px;text-align:center;line-height:32px}
</style>
</head>
<body>

<section class="hero">
  <div class="hero-bg" role="img" aria-label="Airliner landing over a runway at sunset under a deep blue sky"></div>
  <header class="site-header">
    <div class="brand"><span class="brand-dot"></span>SkyGrid</div>
    <nav class="main-nav">
      <a href="#" class="active">HOME</a><a href="#">ABOUT US</a><a href="#">SERVICES</a><a href="#">NEWS</a><a href="#">CONTACT US</a>
      <svg width="14" height="14" viewBox="0 0 14 14" style="margin-left:10px"><circle cx="6" cy="6" r="4.5" fill="none" stroke="#fff" stroke-width="1.6"/><path d="M9.5 9.5 13 13" stroke="#fff" stroke-width="1.6"/></svg>
    </nav>
  </header>
  <h1 class="hero-title">AVIATION. TECHNOLOGY. VISUALIZED</h1>
  <p class="hero-sub"><b>SkyGrid International</b> presents and displays innovative management and technology solutions that address complex noise and airspace issues for airports and residential communities.</p>
  <a class="btn" href="#">READ MORE</a>
  <span class="hero-arrow left"><svg width="12" height="16" viewBox="0 0 12 16"><path d="M9 1 2 8l7 7" fill="none" stroke="#fff" stroke-width="2"/></svg></span>
  <span class="hero-arrow right"><svg width="12" height="16" viewBox="0 0 12 16"><path d="M3 1l7 7-7 7" fill="none" stroke="#fff" stroke-width="2"/></svg></span>
</section>

<section class="about">
  <div class="about-copy">
    <span class="eyebrow">About us</span>
    <h2 class="section-title">WHO WE ARE</h2>
    <div class="rule"></div>
    <p><b>SkyGrid International</b> helps Airports, Air Traffic Organizations, Builders and Architects by analyzing operations, monitoring noise levels and creating software that improves daily operations and public relations.</p>
    <p>We are a small company with a global customer base.</p>
    <p>We're proud to help our customers understand their operations and study their impact on the community through the use of clear software, reports and modern visualization tools.</p>
    <p>Additionally, we actively support the noise and aviation community and share practical knowledge and tools that encourage better decisions.</p>
    <a class="btn" href="#">READ MORE</a>
  </div>
  <div class="about-visual" role="img" aria-label="Business jet flying among clouds in a soft blue sky"></div>
  <div class="about-brand">SkyGrid</div>
</section>

<section class="services">
  <span class="eyebrow">What we do</span>
  <h2 class="section-title">OUR SERVICES</h2>
  <div class="rule"></div>
  <div class="service-grid">
    <div class="service-card"><div class="service-img" role="img" aria-label="Airport terminal with aircraft at the gates"></div><div class="service-label">AIRPORTS</div></div>
    <div class="service-card"><div class="service-img" role="img" aria-label="Laptop and monitors showing flight software"></div><div class="service-label">SOFTWARE</div></div>
    <div class="service-card"><div class="service-img" role="img" aria-label="Jet engine close-up representing noise and emissions"></div><div class="service-label">NOISE &amp; EMISSIONS</div></div>
    <div class="service-card"><div class="service-img" role="img" aria-label="Close-up of an eye representing data visualization"></div><div class="service-label">VISUALIZATION</div></div>
  </div>
</section>

<section class="goals">
  <div class="goal-col">
    <h3>Our Objectives</h3>
    <div class="rule"></div>
    <ul>
      <li>Give confidence to professional and government agencies and industry clients maintaining a variety of noise and accessibility goals.</li>
      <li>Showcase our capabilities and areas of expertise.</li>
      <li>Highlight our software capability through images or demo videos.</li>
    </ul>
  </div>
  <div class="goal-col">
    <h3>Audience</h3>
    <div class="rule"></div>
    <ul>
      <li>Potential customers such as airports, airlines, governments or local developers, builders and engineering support.</li>
      <li>Current clients users looking for software updates, training and support.</li>
      <li>Journalists from industry publications and general media.</li>
    </ul>
  </div>
</section>

<section class="news">
  <div class="news-bg" role="img" aria-label="Faint photo of a drone flying on a light grey background"></div>
  <span class="eyebrow">A glimpse of our blog</span>
  <h2 class="section-title">LATEST NEWS</h2>
  <div class="rule"></div>
  <div class="news-grid">
    <article class="news-card"><div class="news-img" role="img" aria-label="White drone hovering in the air"></div><h4>Lorem ipsum dolor sit amet, consectetur adipiscing elit</h4><div class="news-meta"><span>10 July 2017</span><span>By User Name</span><span>10 Comments</span></div></article>
    <article class="news-card"><div class="news-img" role="img" aria-label="Drone flying against a blue sky"></div><h4>Lorem ipsum dolor sit amet, consectetur adipiscing elit</h4><div class="news-meta"><span>10 July 2017</span><span>By User Name</span><span>10 Comments</span></div></article>
    <article class="news-card"><div class="news-img" role="img" aria-label="Aircraft silhouette on a runway at sunset"></div><h4>Lorem ipsum dolor sit amet, consectetur adipiscing elit</h4><div class="news-meta"><span>10 July 2017</span><span>By User Name</span><span>10 Comments</span></div></article>
  </div>
</section>

<footer class="site-footer">
  <div class="foot-col foot-about">
    <h4>ABOUT SKYGRID</h4><div class="rule"></div>
    <p>SkyGrid International helps airports, air traffic organizations, builders and architects with software and consulting that address complex noise and airspace issues. We analyze operations, monitor noise levels and create software that improves operations, meets customer requirements and supports public relations.</p>
  </div>
  <div class="foot-col foot-links">
    <h4>QUICK LINKS</h4><div class="rule"></div>
    <ul><li>Home</li><li>About Us</li><li>Services</li><li>News</li><li>Contact</li></ul>
  </div>
  <div class="foot-col foot-services">
    <h4>OUR SERVICES</h4><div class="rule"></div>
    <ul><li>Airports</li><li>Software</li><li>Noise &amp; Emissions</li><li>Visualization</li></ul>
  </div>
  <div class="foot-col foot-contact">
    <h4>CONTACT US</h4><div class="rule"></div>
    <div class="contact-row"><svg width="10" height="12" viewBox="0 0 10 12"><path d="M5 0a4 4 0 0 0-4 4c0 3 4 8 4 8s4-5 4-8a4 4 0 0 0-4-4z" fill="#3d8fd9"/></svg><p>2140 Harbor Field Way, Suite 300<br>Lakeview, CA 90000</p></div>
    <div class="contact-row"><svg width="10" height="10" viewBox="0 0 10 10"><path d="M2 0 4 3 3 4c1 2 2 3 3 3l1-1 3 2-1 2C5 10 0 5 0 1z" fill="#3d8fd9"/></svg><p>+1 (555) 010-2233</p></div>
    <div class="contact-row"><svg width="10" height="10" viewBox="0 0 10 10"><path d="M2 0 4 3 3 4c1 2 2 3 3 3l1-1 3 2-1 2C5 10 0 5 0 1z" fill="#3d8fd9"/></svg><p>+1 (555) 010-4455</p></div>
    <div class="contact-row"><svg width="11" height="8" viewBox="0 0 11 8"><rect width="11" height="8" fill="#3d8fd9"/><path d="M0 0l5.5 4L11 0" fill="none" stroke="#0d1f36"/></svg><p>info@skygrid-example.com</p></div>
    <div class="socials"><span></span><span></span><span></span><span></span><span></span></div>
  </div>
</footer>
<div class="foot-bar">© 2018 SkyGrid International. All Rights Reserved.</div>

</body>
</html>
```